Bold and colurful E-liquid Design Template

I'm looking for a new label for my house range of NIMBUS. I currently have almost 40 flavours, so I'm looking for a single label design that I can modify to create the rest of the flavours.
Each label will have the same design, but I'll change the color for each flavour and the name.
I'd like the label to be predominantly text based with bold text and bold colours. I like bold typographic styles. Also for each flavour I'd like to add 1 - 3 letters to represent the flavour. This can be in a larger font.
eg for
Blueberry I'll use the letter B
Pineapple Peach will use PP
Cinnamon Blueberry Muffin uses CBM
The colour used on the label will also be important so they stand out nicely on the shelf.
I've attached a psd mockup of the bottles I'll be using.

```html
<!DOCTYPE html>
<html lang="en">
<head>
<meta charset="utf-8">
<title>Nimbus – Flavour Label Range</title>
<link rel="stylesheet" href="https://fonts.googleapis.com/css2?family=Orbitron:wght@800&display=swap">
<style>
  :root {
    --canvas-bg: #e6e6e8;
    --label-white: #ffffff;
    --accent-cbm: #9b1f5c;
    --accent-pineapple: #f2a53a;
    --accent-blueberry: #25a5e0;
    --ink-light: #ffffff;
  }
  html, body {
    margin: 0;
    padding: 0;
    width: 1098px;
    height: 1200px;
    overflow: hidden;
    background: var(--canvas-bg);
  }
  .label-range {
    width: 1098px;
    height: 1200px;
    display: flex;
    justify-content: center;
    align-items: center;
    gap: 40px;
  }
  .flavour-label {
    width: 300px;
    height: 880px;
    background: var(--label-white);
    box-shadow: 0 6px 18px rgba(0,0,0,0.15);
  }
  .flavour-label svg { display: block; width: 300px; height: 880px; }
  .flavour-label--cbm { --accent: var(--accent-cbm); }
  .flavour-label--pineapple-peach { --accent: var(--accent-pineapple); }
  .flavour-label--blueberry { --accent: var(--accent-blueberry); }

  .accent-fill { fill: var(--accent); }
  .label-type { font-family: 'Orbitron', sans-serif; font-weight: 800; }
  .flavour-name { font-size: 22px; fill: var(--ink-light); }
  .brand-name { font-size: 100px; fill: var(--accent); }
  .quality-line { font-size: 27px; fill: var(--accent); }
  .strength-volume { font-size: 24px; fill: var(--ink-light); }
</style>
</head>
<body>
<main class="label-range">

  <article class="flavour-label flavour-label--cbm">
    <svg viewBox="0 0 300 880" class="label-type">
      <path class="accent-fill" d="M0 0 H300 V125 C235 120 175 140 125 155 C75 170 35 166 0 162 Z"/>
      <text class="flavour-name" x="150" y="82" text-anchor="middle">CBM</text>
      <text class="brand-name" transform="translate(172,690) rotate(-90)" textLength="500">NIMBUS</text>
      <text class="quality-line" transform="translate(226,640) rotate(-90)" textLength="400">PREMIUM QUALITY</text>
      <rect class="accent-fill" x="25" y="725" width="250" height="70"/>
      <text class="strength-volume" x="150" y="769" text-anchor="middle">3MG | 100ML</text>
    </svg>
  </article>

  <article class="flavour-label flavour-label--pineapple-peach">
    <svg viewBox="0 0 300 880" class="label-type">
      <path class="accent-fill" d="M0 0 H300 V125 C235 120 175 140 125 155 C75 170 35 166 0 162 Z"/>
      <text class="flavour-name" x="150" y="82" text-anchor="middle" textLength="284" lengthAdjust="spacingAndGlyphs">PINEAPPLE PEACH</text>
      <text class="brand-name" transform="translate(172,690) rotate(-90)" textLength="500">NIMBUS</text>
      <text class="quality-line" transform="translate(226,640) rotate(-90)" textLength="400">PREMIUM QUALITY</text>
      <rect class="accent-fill" x="25" y="725" width="250" height="70"/>
      <text class="strength-volume" x="150" y="769" text-anchor="middle">3MG | 100ML</text>
    </svg>
  </article>

  <article class="flavour-label flavour-label--blueberry">
    <svg viewBox="0 0 300 880" class="label-type">
      <path class="accent-fill" d="M0 0 H300 V125 C235 120 175 140 125 155 C75 170 35 166 0 162 Z"/>
      <text class="flavour-name" x="150" y="82" text-anchor="middle">BLUEBERRY</text>
      <text class="brand-name" transform="translate(172,690) rotate(-90)" textLength="500">NIMBUS</text>
      <text class="quality-line" transform="translate(226,640) rotate(-90)" textLength="400">PREMIUM QUALITY</text>
      <rect class="accent-fill" x="25" y="725" width="250" height="70"/>
      <text class="strength-volume" x="150" y="769" text-anchor="middle">3MG | 100ML</text>
    </svg>
  </article>

</main>
</body>
</html>
```